Manuka honey wholesales and exports

We need business cards for our honey distribution company based in New Zealand. We supply shops locally and export Manuka honey around the world.
We deal with a very high quality and 100% natural product that can be used for medical, general health as well as food. We are looking business cards that show our honey products are of a high quality with a modern look.

Target Market(s)

Health and medical retailers and importers

Industry/Entity Type

Wholesale

Contact Information for Business Card

Kestrel Hive NZ Limited

www.kestrelhivenz.com

Gareth Moffat

M +64 213958264

E kestrelhivenz@mailbox-example.com

PO Box 47-518
Takapuna
North Shore
Auckland
New Zealand

Font styles to use
Serif

Requirements
Must have
• (Kestrel Hive NZ Limited) with some artwork on one side and all details on the other side.
Nice to have
• I have seen a very simple card with large yellow and black stripes on one side with a company name.. looked clean and simple so something similar or just let the creative beast inside you take over and we will see what you can come up with.

```html
<!DOCTYPE html>
<html lang="en">
<head>
<meta charset="utf-8">
<title>Kestrel Hive NZ Limited – Business Card</title>
<link rel="stylesheet" href="https://fonts.googleapis.com/css2?family=Noto+Serif:wght@400;700&display=swap">
<style>
  :root {
    --honey-yellow: #fdd91c;
    --stripe-white: #ffffff;
    --card-white: #ffffff;
    --ink: #111111;
    --backdrop: #ecebe8;
  }
  * { margin: 0; padding: 0; box-sizing: border-box; }
  html, body {
    width: 1200px;
    height: 1000px;
    overflow: hidden;
    background: var(--backdrop);
  }
  .canvas {
    position: relative;
    width: 1200px;
    height: 1000px;
    font-family: "Noto Serif", serif;
  }
  .card {
    position: absolute;
    box-shadow: 0 4px 14px rgba(0,0,0,0.18);
  }

  /* Front: striped side with company name */
  .card-front {
    left: 60px;
    top: 190px;
    width: 560px;
    height: 330px;
    overflow: hidden;
    background: repeating-linear-gradient(
      30deg,
      var(--honey-yellow) 0 22px,
      var(--stripe-white) 22px 40px
    );
    display: flex;
    align-items: center;
    justify-content: center;
  }
  .name-plate {
    background: var(--honey-yellow);
    padding: 22px 34px;
  }
  .company-name {
    text-align: center;
    font-family: "Noto Serif", serif;
    font-weight: 700;
    color: var(--stripe-white);
    font-size: 21px;
    letter-spacing: 1.5px;
    line-height: 1.3;
    text-transform: uppercase;
  }

  /* Back: details side */
  .card-back {
    left: 620px;
    top: 500px;
    width: 530px;
    height: 300px;
    background: var(--card-white);
    padding: 18px;
  }
  .details-frame {
    width: 100%;
    height: 100%;
    border: 2px solid var(--ink);
    display: flex;
    flex-direction: column;
    align-items: center;
    padding-top: 28px;
    color: var(--ink);
    font-size: 14.5px;
    line-height: 20px;
    text-align: center;
  }
  .person-name {
    font-weight: 700;
    font-size: 24px;
    letter-spacing: 1.5px;
    line-height: 28px;
  }
  .divider {
    width: 62px;
    height: 2px;
    background: var(--ink);
    margin: 12px 0;
  }
  .person-name + .divider { margin-top: 24px; }
</style>
</head>
<body>
<main class="canvas">
  <section class="card card-front" aria-label="Card front">
    <div class="name-plate">
      <p class="company-name">Kestrel Hive<br>NZ Limited</p>
    </div>
  </section>

  <section class="card card-back" aria-label="Card back">
    <div class="details-frame">
      <h1 class="person-name">Gareth Moffat</h1>
      <div class="divider"></div>
      <p class="contact">+64 213958264<br>www.kestrelhivenz.com<br>kestrelhivenz@mailbox-example.com</p>
      <div class="divider"></div>
      <p class="address">PO Box 47-518, Takapuna<br>North Shore, Auckland<br>New Zealand</p>
    </div>
  </section>
</main>
</body>
</html>
```